High End Notary Service Business Card Design

Want a professional and elegant/luxurious business card that is clean and simple in the design. A notary is a trusted professional that helps people sign very important documents. The card should be in alignment with this service provided.

Most of the time, service will be for the purchase of a home or refinance of a mortgage

There is NO LOGO. This is aesthetic. A look and feel. Conveying professionalism and concierge level of service.

Target Market(s)

Other business professionals, Lawyers, Escrow Officers, Loan Officers

Industry/Entity Type

Legal

Contact Information for Business Card

This will be a one-sided business card

Colors
35a7d7
3176b5
85cae6
d3a5cc
b868aa
ffffff
0356a4

Requirements
Must have
• Lorena T. Mirabel-Hodgkins
Notary Public

642-871-3094
MirabelSigningDesk@Wexmail.com
Nice to have
• Headshot photo below. Convey the aspect of signing documents. No black cards. Preference is shades of blue: light blue, navy, aqua, gold, white, or lavendar, etc.
Should not have
• No scales or legal scales.

```html
<!DOCTYPE html>
<html lang="en">
<head>
<meta charset="utf-8">
<title>Notary Public Business Card – Colour Options</title>
<link href="https://fonts.googleapis.com/css2?family=Outfit:wght@300;400;500&display=swap" rel="stylesheet">
<style>
  :root {
    --backdrop: #fde6d6;
    --white: #ffffff;
    --mid-blue: #3176b5;
    --navy: #0356a4;
    --aqua: #35a7d7;
    --light-blue: #85cae6;
    --lavender: #d3a5cc;
    --photo-tone-a: #9aa0ad;
    --photo-tone-b: #c7a48a;
  }
  * { margin: 0; padding: 0; box-sizing: border-box; }
  html, body {
    width: 1200px;
    height: 300px;
    overflow: hidden;
    background: var(--backdrop);
    font-family: "Outfit", "Helvetica Neue", Arial, sans-serif;
  }
  .card-lineup {
    position: relative;
    width: 1200px;
    height: 300px;
  }
  .business-card {
    position: absolute;
    top: 12px;
    width: 175.6px;
    height: 276px;
    box-shadow: 2px 3px 5px rgba(0, 0, 0, 0.22);
  }
  .business-card svg { display: block; width: 100%; height: 100%; }
  .card-blue     { left: 282px;   --panel: var(--mid-blue); --accent: var(--lavender); }
  .card-lavender { left: 512px;   --panel: var(--lavender); --accent: var(--aqua); }
  .card-navy     { left: 742.5px; --panel: var(--navy);     --accent: var(--light-blue); }

  .card-paper { fill: var(--white); }
  .accent-stripe { fill: var(--accent); }
  .colour-panel { fill: var(--panel); }
  .photo-ring { fill: var(--white); }
  .rule { stroke: var(--white); stroke-width: 3; }
  .rule-dot { fill: var(--white); }
  .holder-name { fill: var(--white); font-size: 24px; font-weight: 500; letter-spacing: 0.2px; }
  .holder-title { fill: var(--white); font-size: 14.5px; font-weight: 300; letter-spacing: 0.3px; }
  .contact-line { fill: var(--white); font-size: 14.5px; font-weight: 400; }
  .contact-icon { fill: var(--white); }
  .contact-icon-line { stroke: var(--panel); stroke-width: 1.6; fill: none; }
</style>
</head>
<body>
<main class="card-lineup">

  <article class="business-card card-blue">
    <svg viewBox="0 0 377 592" xmlns="http://www.w3.org/2000/svg">
      <defs>
        <linearGradient id="photoToneBlue" x1="0" y1="0" x2="0" y2="1">
          <stop offset="0" stop-color="#9aa0ad"/>
          <stop offset="0.6" stop-color="#a9a3a6"/>
          <stop offset="1" stop-color="#c7a48a"/>
        </linearGradient>
      </defs>
      <rect class="card-paper" width="377" height="592"/>
      <polygon class="accent-stripe" points="0,312 377,107 377,124 0,328"/>
      <polygon class="colour-panel" points="0,326 377,122 377,592 0,592"/>
      <circle class="photo-ring" cx="188" cy="202" r="116"/>
      <circle cx="188" cy="202" r="100" fill="url(#photoToneBlue)" role="img" aria-label="Headshot of the notary"/>
      <text class="holder-name" x="188" y="369" text-anchor="middle">Lorena T. Mirabel-Hodgkins</text>
      <line class="rule" x1="42" y1="380" x2="335" y2="380"/>
      <circle class="rule-dot" cx="188" cy="380" r="4.5"/>
      <text class="holder-title" x="188" y="404" text-anchor="middle">NOTARY PUBLIC</text>
      <g class="contact-phone">
        <path class="contact-icon" d="M43,507 q8,-6 16,0 l0,3 -4,0 0,-2 q-4,-1 -8,0 l0,2 -4,0 z M45,511 h12 l2,7 h-16 z"/>
        <text class="contact-line" x="71" y="516">642-871-3094</text>
      </g>
      <g class="contact-email">
        <rect class="contact-icon" x="43" y="532" width="16" height="11" rx="1"/>
        <polyline class="contact-icon-line" points="43.5,533 51,539 58.5,533"/>
        <text class="contact-line" x="71" y="543">MirabelSigningDesk@Wexmail.com</text>
      </g>
    </svg>
  </article>

  <article class="business-card card-lavender">
    <svg viewBox="0 0 377 592" xmlns="http://www.w3.org/2000/svg">
      <defs>
        <linearGradient id="photoToneLavender" x1="0" y1="0" x2="0" y2="1">
          <stop offset="0" stop-color="#9aa0ad"/>
          <stop offset="0.6" stop-color="#a9a3a6"/>
          <stop offset="1" stop-color="#c7a48a"/>
        </linearGradient>
      </defs>
      <rect class="card-paper" width="377" height="592"/>
      <polygon class="accent-stripe" points="0,312 377,107 377,124 0,328"/>
      <polygon class="colour-panel" points="0,326 377,122 377,592 0,592"/>
      <circle class="photo-ring" cx="188" cy="202" r="116"/>
      <circle cx="188" cy="202" r="100" fill="url(#photoToneLavender)" role="img" aria-label="Headshot of the notary"/>
      <text class="holder-name" x="188" y="369" text-anchor="middle">Lorena T. Mirabel-Hodgkins</text>
      <line class="rule" x1="42" y1="380" x2="335" y2="380"/>
      <circle class="rule-dot" cx="188" cy="380" r="4.5"/>
      <text class="holder-title" x="188" y="404" text-anchor="middle">NOTARY PUBLIC</text>
      <g class="contact-phone">
        <path class="contact-icon" d="M43,507 q8,-6 16,0 l0,3 -4,0 0,-2 q-4,-1 -8,0 l0,2 -4,0 z M45,511 h12 l2,7 h-16 z"/>
        <text class="contact-line" x="71" y="516">642-871-3094</text>
      </g>
      <g class="contact-email">
        <rect class="contact-icon" x="43" y="532" width="16" height="11" rx="1"/>
        <polyline class="contact-icon-line" points="43.5,533 51,539 58.5,533"/>
        <text class="contact-line" x="71" y="543">MirabelSigningDesk@Wexmail.com</text>
      </g>
    </svg>
  </article>

  <article class="business-card card-navy">
    <svg viewBox="0 0 377 592" xmlns="http://www.w3.org/2000/svg">
      <defs>
        <linearGradient id="photoToneNavy" x1="0" y1="0" x2="0" y2="1">
          <stop offset="0" stop-color="#9aa0ad"/>
          <stop offset="0.6" stop-color="#a9a3a6"/>
          <stop offset="1" stop-color="#c7a48a"/>
        </linearGradient>
      </defs>
      <rect class="card-paper" width="377" height="592"/>
      <polygon class="accent-stripe" points="0,312 377,107 377,124 0,328"/>
      <polygon class="colour-panel" points="0,326 377,122 377,592 0,592"/>
      <circle class="photo-ring" cx="188" cy="202" r="116"/>
      <circle cx="188" cy="202" r="100" fill="url(#photoToneNavy)" role="img" aria-label="Headshot of the notary"/>
      <text class="holder-name" x="188" y="369" text-anchor="middle">Lorena T. Mirabel-Hodgkins</text>
      <line class="rule" x1="42" y1="380" x2="335" y2="380"/>
      <circle class="rule-dot" cx="188" cy="380" r="4.5"/>
      <text class="holder-title" x="188" y="404" text-anchor="middle">NOTARY PUBLIC</text>
      <g class="contact-phone">
        <path class="contact-icon" d="M43,507 q8,-6 16,0 l0,3 -4,0 0,-2 q-4,-1 -8,0 l0,2 -4,0 z M45,511 h12 l2,7 h-16 z"/>
        <text class="contact-line" x="71" y="516">642-871-3094</text>
      </g>
      <g class="contact-email">
        <rect class="contact-icon" x="43" y="532" width="16" height="11" rx="1"/>
        <polyline class="contact-icon-line" points="43.5,533 51,539 58.5,533"/>
        <text class="contact-line" x="71" y="543">MirabelSigningDesk@Wexmail.com</text>
      </g>
    </svg>
  </article>

</main>
</body>
</html>
```